Marolina Swimming & Athletics Center

We need Business Card for a Athletics center
The logo frome the Uploaded Files ( b card fimal)
Οn one side of card we need the logo of company the Contact and the website:
1. Address:(Limassol, Cyprus 12-14 Dravelonos str,Ano Feralia,P.C. 5280)

2.Phone number: (+357) 25-804273

3. Mail: info@marolinasport.example

3. Website: www.marolinasport.example

Οn the other side of the card we need to write the sport of the company:

1. Artistic Gymnastics
2. Swimming
3. Gym - Fitness
4. Programs
5. Dancing
5.Tennis

From the Uploaded Files you can get the logo.In a logo is behind the black color which can be removed from logo.

Υou can use that color you want.
.

Industry/Entity Type

Business

Font styles to use
Decorative

Colors
0555a3
ffcf3e
3176b5
0692cd
add136
f04a50
000000
cfcfcf
9d9d9d

Requirements
Should not have
• photos with faces
• photo fro the Website:www.marolinasport.example

```html
<!DOCTYPE html>
<html lang="en">
<head>
<meta charset="utf-8">
<title>Marolina Swimming &amp; Athletics Center – Business Card</title>
<link rel="stylesheet" href="https://fonts.googleapis.com/css2?family=Montserrat:wght@400;500;700;800&display=swap">
<style>
  :root {
    --backdrop: #2e2e2e;
    --card-dark: #000000;
    --card-light: #ffffff;
    --gold: #ffcf3e;
    --blue-bright: #0692cd;
    --blue-deep: #0555a3;
    --ink: #1a1a1a;
    --soft-grey: #cfcfcf;
    --mid-grey: #9d9d9d;
  }
  * { margin: 0; padding: 0; box-sizing: border-box; }
  html, body { width: 1200px; height: 900px; overflow: hidden; }
  body {
    background: var(--backdrop);
    font-family: "Montserrat", Arial, sans-serif;
    position: relative;
  }
  .card {
    position: absolute;
    width: 700px;
    height: 400px;
    left: 250px;
    border-radius: 24px;
    overflow: hidden;
    box-shadow: 0 14px 30px rgba(0,0,0,0.45);
  }
  /* Front side */
  .card-front { top: 35px; background: var(--card-dark); color: #fff; }
  .brand-row {
    position: absolute; left: 60px; top: 60px;
    display: flex; align-items: center; gap: 26px;
  }
  .brand-name {
    font-weight: 800; font-size: 70px; letter-spacing: 2px;
    color: var(--gold); line-height: 1; white-space: nowrap;
  }
  .brand-dot {
    width: 96px; height: 96px; border-radius: 50%;
    border: 4px solid var(--gold); flex: none;
  }
  .sport-list {
    position: absolute; left: 60px; bottom: 50px;
    list-style: none;
  }
  .sport-list li {
    font-size: 17px; font-weight: 500; letter-spacing: 0.5px;
    line-height: 25px; text-transform: uppercase;
    display: flex; align-items: center; gap: 14px;
  }
  .sport-list li::before {
    content: ""; width: 9px; height: 9px; border-radius: 50%;
    background: var(--gold);
  }
  .front-web {
    position: absolute; right: 50px; top: 200px;
    font-size: 19px; font-weight: 500; white-space: nowrap;
  }
  .front-web .domain { color: var(--gold); font-weight: 700; }

  /* Back side */
  .card-back { top: 470px; background: var(--card-light); color: var(--ink); }
  .side-tab {
    position: absolute; left: 0; top: 120px;
    width: 18px; height: 44px; background: var(--card-dark);
  }
  .person { position: absolute; left: 50px; top: 112px; }
  .person-name { font-size: 32px; font-weight: 700; color: var(--blue-bright); }
  .person-role { font-size: 16px; font-weight: 500; margin-top: 2px; }
  .address {
    position: absolute; left: 50px; top: 205px;
    font-size: 16px; line-height: 22px;
  }
  .contacts { position: absolute; left: 50px; bottom: 38px; list-style: none; }
  .contacts li {
    display: flex; align-items: center; gap: 12px;
    font-size: 17px; line-height: 27px; white-space: nowrap;
  }
  .contacts svg { width: 14px; height: 14px; fill: var(--blue-bright); flex: none; }
  .contacts .domain { color: var(--blue-deep); font-weight: 700; }
  .back-brand {
    position: absolute; right: 50px; top: 60px;
    display: flex; flex-direction: column; align-items: center; gap: 16px;
  }
  .back-brand .brand-dot {
    width: 190px; height: 190px; border: 6px solid var(--gold);
    background: var(--card-dark);
  }
  .back-brand .brand-name { font-size: 34px; color: var(--card-dark); letter-spacing: 2px; }
</style>
</head>
<body>
  <section class="card card-front" aria-label="Card front">
    <div class="brand-row">
      <span class="brand-name">MAROLINA</span>
      <span class="brand-dot"></span>
    </div>
    <ul class="sport-list">
      <li>Artistic Gymnastics</li>
      <li>Swimming</li>
      <li>Gym - Fitness</li>
      <li>Programs</li>
      <li>Dancing</li>
      <li>Tennis</li>
    </ul>
    <p class="front-web">www.<span class="domain">marolinasport</span>.example</p>
  </section>

  <section class="card card-back" aria-label="Card back">
    <span class="side-tab"></span>
    <div class="person">
      <h1 class="person-name">Marcus Ellery</h1>
      <p class="person-role">Director</p>
    </div>
    <p class="address">Limassol, Cyprus<br>12-14 Dravelonos<br>str,Ano Feralia,P.C. 5280</p>
    <ul class="contacts">
      <li><svg viewBox="0 0 24 24"><path d="M6.6 10.8a15 15 0 0 0 6.6 6.6l2.2-2.2a1 1 0 0 1 1-.25 11.4 11.4 0 0 0 3.6.57 1 1 0 0 1 1 1V20a1 1 0 0 1-1 1A17 17 0 0 1 3 4a1 1 0 0 1 1-1h3.5a1 1 0 0 1 1 1c0 1.25.2 2.45.57 3.57a1 1 0 0 1-.25 1z"/></svg><span>(+357) 25-804273</span></li>
      <li><svg viewBox="0 0 24 24"><path d="M2 5h20v14H2zm2 2v.5l8 5 8-5V7zm0 2.8V17h16V9.8l-8 5z"/></svg><span>info@marolinasport.example</span></li>
      <li><svg viewBox="0 0 24 24"><path d="M12 2a10 10 0 1 0 0 20 10 10 0 0 0 0-20zm6.9 9h-3a15 15 0 0 0-1.2-5.4A8 8 0 0 1 18.9 11zM12 4.1c.9 1.2 1.8 3.6 1.9 6.9h-3.8c.1-3.3 1-5.7 1.9-6.9zM9.3 5.6A15 15 0 0 0 8.1 11h-3a8 8 0 0 1 4.2-5.4zM5.1 13h3a15 15 0 0 0 1.2 5.4A8 8 0 0 1 5.1 13zm6.9 6.9c-.9-1.2-1.8-3.6-1.9-6.9h3.8c-.1 3.3-1 5.7-1.9 6.9zm2.7-1.5a15 15 0 0 0 1.2-5.4h3a8 8 0 0 1-4.2 5.4z"/></svg><span>www.<span class="domain">marolinasport</span>.example</span></li>
    </ul>
    <div class="back-brand">
      <span class="brand-dot"></span>
      <span class="brand-name">MAROLINA</span>
    </div>
  </section>
</body>
</html>
```